Adventure Business Cards

Please check out our website for style
Vertical card
Details:
Side 1
Logo
Business name: Kestrel Point Wildland Tours
Name: Colin Warbeck
Role: Director
Email: info@kestrelpointtours.com
Address: PO Box 71, Marlin Cove NSW 2471
Phone: +61 2 5550 1847
Web address: www.kestrelpointtours.com
Side 2
Taking pictures?
A Friendwall and Pixlane logo
Tag us in your pictures with
#kpwildtours
@kpwildtours
www.kestrelpointtours.com
Details:
Side 1
Logo
Name: Colin Warbeck
Role: Director
Phone: +61 2 5550 1847
Side 2
Taking pictures?
#kpwildtours
@kpwildtours

```html
<!DOCTYPE html>
<html lang="en">
<head>
<meta charset="utf-8">
<title>Kestrel Point Wildland Tours – Business Card</title>
<link href="https://fonts.googleapis.com/css2?family=Questrial&family=PT+Sans&display=swap" rel="stylesheet">
<style>
  :root {
    --page: #e9e6e2;
    --ink: #000000;
    --white: #ffffff;
    --yellow: #f3e12a;
    --dusk-top: #d8913c;
    --dusk-low: #f5e33e;
    --sea-top: #3670a8;
    --sea-mid: #3d73aa;
    --sea-low: #93c4d0;
  }
  html, body { margin: 0; width: 1200px; height: 1200px; overflow: hidden; background: var(--page); }
  .canvas { position: relative; width: 1200px; height: 1200px; }
  .card { position: absolute; top: 228px; width: 426px; height: 746px; overflow: hidden; box-shadow: 0 4px 10px rgba(0,0,0,.25); }

  /* Front */
  .card--front { left: 148px; background: var(--ink); font-family: "Questrial", sans-serif; color: var(--white); }
  .scenery { position: absolute; left: 0; top: 0; width: 426px; height: 330px; background: linear-gradient(to bottom, var(--dusk-top) 0, var(--dusk-low) 100%); }
  .brand { position: absolute; left: 0; width: 426px; top: 110px; display: flex; flex-direction: column; align-items: center; gap: 10px; }
  .brand__dot { width: 26px; height: 26px; border-radius: 50%; background: var(--ink); }
  .brand__name { font-size: 24px; line-height: 1.2; color: var(--ink); text-align: center; }
  .person { position: absolute; left: 36px; top: 458px; }
  .person__name { font-size: 25px; margin: 0; font-weight: 400; letter-spacing: .5px; }
  .person__role { font-size: 17px; color: var(--yellow); margin-top: 4px; }
  .contacts { position: absolute; left: 36px; top: 550px; list-style: none; margin: 0; padding: 0; font-size: 18px; }
  .contacts li { display: flex; align-items: center; gap: 10px; height: 25px; }
  .contacts svg { width: 16px; height: 16px; flex: none; }
  .address { position: absolute; left: 36px; top: 645px; font-size: 18px; letter-spacing: .3px; }

  /* Back */
  .card--back { left: 625px; background: linear-gradient(to bottom, var(--sea-top) 0, var(--sea-mid) 52%, var(--sea-low) 100%); font-family: "PT Sans", sans-serif; color: var(--white); text-align: center; }
  .back__title { position: absolute; top: 162px; width: 100%; margin: 0; font-size: 41px; font-weight: 400; }
  .networks { position: absolute; top: 272px; width: 100%; display: flex; justify-content: center; gap: 24px; }
  .network { display: flex; align-items: center; gap: 8px; font-size: 24px; color: var(--ink); }
  .network__mark { width: 22px; height: 22px; background: var(--ink); border-radius: 3px; }
  .back__tag { position: absolute; top: 364px; width: 100%; font-size: 29px; }
  .handles { position: absolute; top: 434px; width: 100%; font-size: 30px; line-height: 36px; }
  .back__web { position: absolute; top: 691px; width: 100%; font-size: 23px; color: var(--ink); }
</style>
</head>
<body>
<main class="canvas">
  <section class="card card--front" aria-label="Card front">
    <div class="scenery" role="img" aria-label="Sunset sky over a dark island mountain silhouette"></div>
    <div class="brand">
      <span class="brand__dot"></span>
      <span class="brand__name">Kestrel Point<br>Wildland Tours</span>
    </div>
    <div class="person">
      <h1 class="person__name">Colin Warbeck</h1>
      <div class="person__role">Director</div>
    </div>
    <ul class="contacts">
      <li><svg viewBox="0 0 16 16"><rect x="1" y="3" width="14" height="10" fill="var(--yellow)"/><path d="M1 3 L8 9 L15 3 M1 13 L6 8 M15 13 L10 8" stroke="var(--ink)" stroke-width="1.2" fill="none"/></svg>info@kestrelpointtours.com</li>
      <li><svg viewBox="0 0 16 16"><path d="M1 6 Q8 1 15 6 L13 8 L11 6.5 L5 6.5 L3 8 Z" fill="var(--yellow)"/><rect x="3" y="8" width="10" height="6" rx="1" fill="var(--yellow)"/><circle cx="8" cy="11" r="1.6" fill="var(--ink)"/></svg>+61 2 5550 1847</li>
      <li><svg viewBox="0 0 16 16"><circle cx="8" cy="8" r="7" fill="var(--yellow)"/><path d="M1 8 H15 M8 1 V15 M3 4.5 H13 M3 11.5 H13" stroke="var(--ink)" stroke-width="1"/><ellipse cx="8" cy="8" rx="3" ry="7" fill="none" stroke="var(--ink)" stroke-width="1"/></svg>www.kestrelpointtours.com</li>
    </ul>
    <div class="address">PO Box 71, Marlin Cove NSW 2471</div>
  </section>

  <section class="card card--back" aria-label="Card back">
    <h2 class="back__title">Taking pictures?</h2>
    <div class="networks">
      <span class="network"><span class="network__mark"></span>Friendwall</span>
      <span class="network"><span class="network__mark"></span>Pixlane</span>
    </div>
    <div class="back__tag">Tag us in your pictures with</div>
    <div class="handles">#kpwildtours<br>@kpwildtours</div>
    <div class="back__web">www.kestrelpointtours.com</div>
  </section>
</main>
</body>
</html>
```